【依頼の目的/概要】
電子書籍(lumora)の表紙デザインをお願いします。
【画像サイズ】※QMSより抜粋
表紙ファイルの理想的な寸法は2560×1600ピクセルです。
注:画像の寸法は1000×625ピクセル以上であることが必要です。
画像の最大の寸法は10000×10000ピクセルです。

【タイトル】
「森と響きあう内なる治癒の道」
サブキャッチ
「もうガンもウイルスも怖くない」 「30年の医療現場で私が感じたこと」
「輝く人生を送るための幸せ健康学」「歴史とデータから浮かび上がる真実」など。
【著者】
看護師30年
堀田みき

【本の内容】
病院や薬に依存し続けてきた結果の日本の現状を歴史やデータから検証。
西洋医学以前の医療に着目し自然免疫の力で健康を取り戻せることが出来ることをお伝えした本です。
※本文を参考資料として添付します。

【デザイン要望】
内容が少し専門的なのですが特に一般の方に読んでいただきたいのであまり堅苦しくない印象のものを考えてはいますが、特に要望はありませんので自由な発想でのご応募を楽しみにしています。
※次点 次々点の方への参加報酬を設定いたしました。
※その他、必要な情報がありましたらお問い合わせください。
宜しくお願いいたします。

どの作品も本当に素晴らしく最後まで悩みに悩みました。内容は医療系なのですが特に一般の方に手にとっていただきたいことから表紙と内容のギャップがないものをと思うとデザインが気に入っても、本の内容で表紙のイメージと全然違うとガッカリされないかなど考え非常に悩みました。タイトルとサブキャッチの大きさや色使い、堅苦しくない明るいデザインが私のイメージと合いましたのでtorvel様のデザインを選ばせていただきました。

今回ピクモアさんに初めて表紙の依頼をさせていただきました。デザイナーさんたちのレベルの高さに感動しておりました。
どのデザインもそれぞれが個性的で本当に素晴らしく最後の最後まで迷っておりました。
今回の本の内容と、専門的ではあるのですが一般向けにしたいということで悩んだ末そちらの視点から一点決めさせていただきました。
1点しか選べないことが心苦しいです。
皆さまお忙しい中、貴重なお時間を割いていただき本当にありがとうございました。
心から感謝しております。

```html
<!DOCTYPE html>
<html lang="ja">
<head>
<meta charset="UTF-8">
<title>森と響きあう内なる治癒の道 — 表紙</title>
<link href="https://fonts.googleapis.com/css2?family=Zen+Maru+Gothic:wght@500;700;900&family=M+PLUS+Rounded+1c:wght@500;700;800&display=swap" rel="stylesheet">
<style>
  :root {
    --night: #1f2a4d;
    --night-deep: #17203f;
    --stripe: rgba(255,255,255,0.035);
    --cream: #fbf6ea;
    --gold: #c9a55c;
    --gold-deep: #a9823a;
    --ink-brown: #8a6a33;
    --ink-dark: #2a2f45;
    --white: #ffffff;
    --ribbon-text: #fff8e8;
  }
  * { margin: 0; padding: 0; box-sizing: border-box; }
  html, body { width: 750px; height: 1200px; overflow: hidden; background: var(--night); }
  .cover {
    position: relative;
    width: 750px; height: 1200px;
    overflow: hidden;
    background:
      repeating-linear-gradient(120deg, var(--stripe) 0 40px, transparent 40px 110px),
      linear-gradient(180deg, var(--night) 0%, var(--night-deep) 100%);
    font-family: "Zen Maru Gothic", "M PLUS Rounded 1c", sans-serif;
  }
  .sky-art { position: absolute; }
  .sky-art--cloud-top { left: 30px; top: 45px; width: 170px; height: 60px; border-radius: 30px;
    background: radial-gradient(ellipse at center, rgba(239,233,220,0.4), rgba(239,233,220,0) 70%); }
  .sky-art--planet { left: 645px; top: 35px; width: 64px; height: 64px; border-radius: 50%;
    background: radial-gradient(circle at 40% 40%, rgba(201,165,92,0.45), rgba(201,165,92,0) 70%); }
  .sky-art--cloud-right { left: 610px; top: 140px; width: 120px; height: 50px; border-radius: 25px;
    background: radial-gradient(ellipse at center, rgba(239,233,220,0.35), rgba(239,233,220,0) 70%); }

  .frame { position: absolute; left: 0; top: 0; width: 750px; height: 1200px; }

  .title { position: absolute; left: 0; width: 750px; text-align: center; color: var(--ink-brown);
    font-weight: 900; letter-spacing: 4px; font-size: 80px; line-height: 1; }
  .title--line1 { top: 220px; }
  .title--line2 { top: 312px; }

  .title-band { position: absolute; left: 135px; top: 412px; width: 480px; height: 88px;
    background: var(--gold); border-radius: 44px; display: flex; align-items: center; justify-content: center;
    color: var(--ink-dark); font-size: 62px; font-weight: 900; letter-spacing: 3px;
    box-shadow: inset 0 0 0 4px var(--cream), inset 0 0 0 6px var(--gold-deep); }

  .author { position: absolute; left: 0; width: 750px; top: 540px; text-align: center; color: var(--ink-brown); }
  .author__career { font-size: 24px; font-weight: 700; margin-right: 14px; vertical-align: middle; }
  .author__name { font-size: 44px; font-weight: 900; letter-spacing: 4px; vertical-align: middle; }

  .figure-art { position: absolute; left: 140px; top: 605px; width: 470px; height: 215px; border-radius: 50% 50% 45% 45%;
    background: radial-gradient(ellipse at 55% 50%, rgba(232,160,90,0.45), rgba(232,160,90,0.12) 55%, rgba(232,160,90,0) 75%); }
  .figure-note { position: absolute; left: 250px; top: 640px; font-size: 20px; font-weight: 700;
    color: var(--ink-dark); line-height: 1.3; }

  .catch { position: absolute; left: 0; top: 860px; width: 750px; height: 140px; color: var(--white);
    font-family: "M PLUS Rounded 1c", sans-serif; }
  .catch__small { position: absolute; left: 30px; font-size: 48px; font-weight: 800; line-height: 1; white-space: nowrap; }
  .catch__small--first { top: 18px; }
  .catch__small--second { top: 80px; }
  .catch__big { position: absolute; right: 26px; top: 14px; white-space: nowrap; font-size: 84px; font-weight: 800; line-height: 1; }

  .sub-ribbon { position: absolute; left: 30px; top: 1020px; width: 690px; height: 58px;
    background: var(--gold-deep); transform: rotate(-3deg); display: flex; align-items: center; justify-content: center;
    color: var(--ribbon-text); font-size: 34px; font-weight: 700; letter-spacing: 2px; }
</style>
</head>
<body>
<main class="cover">
  <div class="sky-art sky-art--cloud-top" role="img" aria-label="夜空に浮かぶ雲と星のイラスト"></div>
  <div class="sky-art sky-art--planet" role="img" aria-label="土星のような惑星のイラスト"></div>
  <div class="sky-art sky-art--cloud-right" role="img" aria-label="右上の雲と星座のイラスト"></div>

  <svg class="frame" viewBox="0 0 750 1200" aria-hidden="true">
    <ellipse cx="375" cy="462" rx="318" ry="368" fill="none" stroke="var(--gold)" stroke-width="3"/>
    <ellipse cx="375" cy="462" rx="304" ry="354" fill="var(--cream)"/>
    <ellipse cx="375" cy="462" rx="290" ry="340" fill="none" stroke="var(--gold)" stroke-width="2" stroke-dasharray="2 8" stroke-linecap="round"/>
  </svg>

  <h1>
    <span class="title title--line1">森と響きあう</span>
    <span class="title title--line2">内なる</span>
    <span class="title-band">治癒の道</span>
  </h1>

  <p class="author"><span class="author__career">看護師30年</span><span class="author__name">堀田 みき</span></p>

  <div class="figure-art" role="img" aria-label="雲の上をふわりと浮かぶ女性と雲のイラスト"></div>
  <p class="figure-note">人間も<br>自然の一部です</p>

  <p class="catch">
    <span class="catch__small catch__small--first">もうガンも</span>
    <span class="catch__small catch__small--second">ウイルスも</span>
    <span class="catch__big">怖くない!</span>
  </p>

  <p class="sub-ribbon">輝く人生を送るための幸せ健康学</p>
</main>
</body>
</html>
```